Wordpress theme website for professionals working together

My partner and I are offering business services, my wife in the energy business as mainly as member of the board of commissioners. I am working as interim manager/consultant in the accounting and finance area. Both activities are connected in one company VELMORO BV (dutch ltd). We need a CV based website. Beside this we do some financial and accounting services.

Target Market(s)

small medium business

Font styles to use
Sans Serif

Colors

Designer to choose colors to be used in the design.

Requirements
Must have
• Pictures of both members.
• CLEAN AND SIMPLE
• I LIKE BLACK & WHITE
Nice to have
• I like design like this theme: http://theme.brindlepax.com/resume/

```html
<!DOCTYPE html>
<html lang="en">
<head>
<meta charset="utf-8">
<title>VELMORO BV – Resume</title>
<link rel="stylesheet" href="https://fonts.googleapis.com/css2?family=Montserrat:wght@600;700&family=Poppins:wght@400;500;600&display=swap">
<style>
:root{
  --dark:#2f2f30;
  --dark-2:#3a3a3b;
  --stone:#5f5858;
  --red:#d14d4d;
  --red-deep:#5a0a0a;
  --pink:#f0a3a3;
  --white:#ffffff;
  --track:#e3e1e1;
  --line:#2b2626;
}
*{box-sizing:border-box;margin:0;padding:0}
html,body{width:1200px;height:2332px;overflow:hidden;background:var(--white)}
body{position:relative;font-family:"Poppins",Arial,sans-serif;color:var(--white)}
.abs{position:absolute}
.header-band{left:0;top:0;width:1200px;height:576px;background:linear-gradient(135deg,var(--dark) 0%,var(--dark-2) 45%,var(--dark) 100%)}
.body-band{left:0;top:578px;width:1200px;height:1694px;background:var(--stone)}
.logo{left:112px;top:38px;font-family:"Montserrat",Arial,sans-serif;font-weight:700;font-size:26px;letter-spacing:.5px}
.nav{top:42px;font-family:"Montserrat",Arial,sans-serif;font-weight:600;font-size:15px}
.hero-shape{left:112px;top:100px}
.photo{left:146px;top:138px;width:398px;height:398px;border-radius:50%;border:5px solid var(--pink);background:radial-gradient(circle at 50% 40%,#d9cfc8 0%,#b8aba3 45%,#5d6370 100%)}
.toggle{left:597px;top:171px;width:199px;height:47px;border:3px solid var(--white);border-radius:24px;overflow:hidden;display:flex;font-weight:600;font-size:18px}
.toggle span{flex:1;display:flex;align-items:center;justify-content:center}
.toggle .on{background:linear-gradient(90deg,#c23c3c,#a82a2a);color:var(--white)}
.toggle .off{background:var(--white);color:var(--red)}
.bio{left:600px;width:400px}
.bio-name{top:247px;font-size:21px;font-weight:600}
.bio-name span{font-weight:500}
.bio-title{top:293px;font-size:21px;font-weight:600}
.bio-job{font-size:16px;font-weight:600;line-height:22px}
.bio-job span{font-size:15px}
.social{top:476px;left:598px;display:flex;gap:10px}
.social i{display:block;width:42px;height:42px;border-radius:50%;background:var(--white)}
.h2{font-family:"Montserrat",Arial,sans-serif;font-weight:700;font-size:27px}
.about-text{left:112px;top:786px;width:488px;font-size:13.5px;line-height:24.5px;text-align:justify}
.btn{left:112px;top:935px;width:110px;height:46px;border:3px solid var(--white);border-radius:23px;font-size:13px;font-weight:500;display:flex;align-items:center;justify-content:center}
.jobs{left:668px;top:744px;width:420px}
.job{margin-bottom:25px}
.job b{display:block;font-size:20px;font-weight:600;line-height:28px}
.job b span{font-size:18px;font-weight:500}
.job p{font-size:17px;font-weight:500;line-height:26px}
.rule{left:112px;width:976px;height:1px;background:var(--line)}
.center{left:0;width:1200px;text-align:center}
.skill{width:456px;height:100px}
.skill-label{font-size:19px;font-weight:500;line-height:26px}
.track{position:absolute;left:0;top:34px;width:456px;height:12px;border-radius:6px;background:var(--track);border:1px solid #c9c4c4}
.fill{position:absolute;left:0;top:0;height:100%;border-radius:6px;background:var(--red)}
.knob{position:absolute;top:-10px;width:30px;height:30px;margin-left:-15px;border-radius:50%;background:var(--red);border:3px solid var(--white)}
.pct{position:absolute;top:60px;width:60px;margin-left:-30px;text-align:center;font-size:16px;font-weight:500}
.pro{width:200px;height:200px;margin-left:-100px;margin-top:-100px;border:4px solid var(--white);border-radius:50%}
.pro-icon{width:70px;height:70px;margin-left:-35px;margin-top:-35px;border-radius:50%;background:var(--red);border:3px solid var(--white);display:flex;align-items:center;justify-content:center}
.pro-text{width:200px;margin-left:-100px;text-align:center}
.pro-text b{display:block;font-family:"Montserrat",Arial,sans-serif;font-size:17px;font-weight:700;margin-bottom:6px}
.pro-text p{font-size:16px;line-height:23px}
.footer-shape{left:112px;top:2126px}
.footer-title{top:2198px}
.copyright{left:112px;top:2272px;width:976px;height:60px;background:var(--red);border-top:1px solid #b53c3c;display:flex;align-items:center;justify-content:center;font-size:14px;font-weight:500}
</style>
</head>
<body>
<div class="abs header-band"></div>
<div class="abs body-band"></div>

<header>
  <div class="abs logo">VELMORO BV</div>
  <nav>
    <span class="abs nav" style="left:615px">HOME</span>
    <span class="abs nav" style="left:704px">PORTFOLIO</span>
    <span class="abs nav" style="left:833px">PAGES</span>
    <span class="abs nav" style="left:926px">BLOG</span>
    <span class="abs nav" style="left:1013px">CONTACT</span>
  </nav>
</header>

<section class="hero">
  <svg class="abs hero-shape" width="976" height="568" viewBox="0 0 976 568">
    <polygon points="0,0 976,0 976,476 488,565 0,476" fill="#d14d4d"/>
    <polyline points="0,477 488,565 976,477" fill="none" stroke="#5a0a0a" stroke-width="5"/>
  </svg>
  <div class="abs photo" role="img" aria-label="Portrait photo of Hugo"></div>
  <div class="abs toggle"><span class="on">Hugo</span><span class="off">Marit</span></div>
  <div class="abs bio bio-name">Name: <span>Hugo</span></div>
  <div class="abs bio bio-title">Actual Jobs:</div>
  <div class="abs bio bio-job" style="top:340px">Advisor WDL: <span>Nemo enim ipsam voluptatem quia voluptas sit aspernatur aut odit.</span></div>
  <div class="abs bio bio-job" style="top:400px">Advisor How &amp; knower: <span>Nemo enim ipsam quia voluptas sit aspernatur aut odit.</span></div>
  <div class="abs social" aria-label="Social links"><i></i><i></i><i></i><i></i><i></i></div>
</section>

<section class="about">
  <div class="abs h2" style="left:112px;top:734px">ABOUT ME</div>
  <p class="abs about-text">Nemo enim ipsam voluptatem quia voluptas sit aspernatur aut odit aut fugit, sed quia consequuntur magni dolores eos qui ratione voluptatem sequi nesciunt. Neque porro quisquam est, qui dolorem ipsum quia dolor sit amet, consectetur, adipisci velit, sed quia non numquam eius modi tempora incidunt ut labore et dolore magnam.</p>
  <div class="abs btn">Read More</div>
  <div class="abs jobs">
    <div class="job"><b>Finished Jobs: <span>Controller a.i. WDL</span></b><p>Sed ut perspiciatis unde omnis iste natus</p></div>
    <div class="job"><b>Advisor Delta Fern</b><p>Sed ut perspiciatis unde omnis iste natus</p></div>
    <div class="job"><b>Financial director EVO</b><p>Sed ut perspiciatis unde omnis iste natus</p></div>
  </div>
</section>

<div class="abs rule" style="top:1044px"></div>

<section class="skills">
  <div class="abs h2 center" style="top:1101px">MY SKILLS</div>

  <div class="abs skill" style="left:112px;top:1190px"><div class="skill-label">Annual Reporting</div><div class="track"><div class="fill" style="width:78%"></div><div class="knob" style="left:78%"></div></div><div class="pct" style="left:78%">90%</div></div>
  <div class="abs skill" style="left:112px;top:1293px"><div class="skill-label">Financial Monthly Reporting</div><div class="track"><div class="fill" style="width:69%"></div><div class="knob" style="left:69%"></div></div><div class="pct" style="left:69%">80%</div></div>
  <div class="abs skill" style="left:112px;top:1396px"><div class="skill-label">Accounting</div><div class="track"><div class="fill" style="width:97%"></div><div class="knob" style="left:97%"></div></div><div class="pct" style="left:97%">100%</div></div>
  <div class="abs skill" style="left:112px;top:1499px"><div class="skill-label">Financial Management</div><div class="track"><div class="fill" style="width:62%"></div><div class="knob" style="left:62%"></div></div><div class="pct" style="left:62%">70%</div></div>

  <div class="abs skill" style="left:631px;top:1190px"><div class="skill-label">Project Management</div><div class="track"><div class="fill" style="width:78%"></div><div class="knob" style="left:78%"></div></div><div class="pct" style="left:78%">90%</div></div>
  <div class="abs skill" style="left:631px;top:1293px"><div class="skill-label">Team Player</div><div class="track"><div class="fill" style="width:69%"></div><div class="knob" style="left:69%"></div></div><div class="pct" style="left:69%">80%</div></div>
  <div class="abs skill" style="left:631px;top:1396px"><div class="skill-label">Trouble Shooter</div><div class="track"><div class="fill" style="width:97%"></div><div class="knob" style="left:97%"></div></div><div class="pct" style="left:97%">100%</div></div>
  <div class="abs skill" style="left:631px;top:1499px"><div class="skill-label">ETC</div><div class="track"><div class="fill" style="width:62%"></div><div class="knob" style="left:62%"></div></div><div class="pct" style="left:62%">70%</div></div>
</section>

<div class="abs rule" style="top:1672px"></div>

<section class="professional">
  <div class="abs h2 center" style="top:1727px">PROFESSIONAL SKILLS</div>

  <div class="abs pro" style="left:323px;top:1946px"></div>
  <div class="abs pro-icon" style="left:323px;top:1854px">
    <svg width="34" height="34" viewBox="0 0 34 34" fill="none" stroke="#fff" stroke-width="2"><rect x="4" y="5" width="18" height="24" rx="2"/><line x1="8" y1="11" x2="18" y2="11"/><line x1="8" y1="16" x2="15" y2="16"/><path d="M28 9 L17 24 L15 28 L19 26 L30 11 Z"/></svg>
  </div>
  <div class="abs pro-text" style="left:323px;top:1915px"><b>EDUCATION</b><p>Norva (RA)<br>Atheneum B</p></div>

  <div class="abs pro" style="left:600px;top:1946px"></div>
  <div class="abs pro-icon" style="left:600px;top:1854px">
    <svg width="34" height="34" viewBox="0 0 34 34" fill="none" stroke="#fff" stroke-width="2"><rect x="4" y="10" width="26" height="18" rx="2"/><path d="M12 10 V6 H22 V10"/><line x1="4" y1="18" x2="30" y2="18"/><rect x="15" y="16" width="4" height="4"/></svg>
  </div>
  <div class="abs pro-text" style="left:600px;top:1915px"><b>WORKED FOR</b><p>TARN Advocaten &amp;<br>Notarissen<br>KVRN</p></div>

  <div class="abs pro" style="left:883px;top:1946px"></div>
  <div class="abs pro-icon" style="left:883px;top:1854px">
    <svg width="34" height="34" viewBox="0 0 34 34" fill="none" stroke="#fff" stroke-width="2"><path d="M10 30 V24 C6 21 5 17 6 13 C8 6 16 3 22 6 C27 9 29 14 27 19 L29 22 H26 V26 H21 V30"/><circle cx="17" cy="14" r="4"/></svg>
  </div>
  <div class="abs pro-text" style="left:883px;top:1915px"><b>OTHER</b><p>Fotography</p></div>
</section>

<footer>
  <svg class="abs footer-shape" width="976" height="146" viewBox="0 0 976 146">
    <polygon points="0,86 488,2 976,86 976,146 0,146" fill="#d14d4d"/>
    <polyline points="0,86 488,2 976,86" fill="none" stroke="#5a0a0a" stroke-width="5"/>
  </svg>
  <div class="abs h2 center footer-title">VELMORO BV</div>
  <div class="abs copyright">Copyrights @ 2018 VELMORO BV. All Rights Reserved.</div>
</footer>
</body>
</html>
```